Business cards for education company

We need a business card design for a relatively new company based in Queensland and operating across Australia. We resell diploma level education courses which include Business, Management, Finance, Community Services & Government courses. We offer over 20 different courses.
The target market is for anyone 16 years of age and older. There is no age limit.

We would like to see the design use the color blue and silver. The final design should communicate professionalism and a bright future.

We sell education but are also promoting the career they see themselves in 2-3 years in the future

Our company logo is attached.

Target Market(s)

We target all age groups above 16 years of age. The main target market would be people aged between 17-35.

We focus on those people who cannot make it into University or do not want to commit the time to a full degree.

Industry/Entity Type

Education

Requirements
Must have
• Professional
Company logo
website
Contact details:

Please use the following example:

Lionel Tapping
Senior Education Consultant
0417 385 960
Lionel.tapping@skylarklearninghub.com.au
www.skylarklearninghub.com.au

```html
<!DOCTYPE html>
<html lang="en">
<head>
<meta charset="utf-8">
<title>Skylark Learning Hub – Business Card</title>
<link rel="stylesheet" href="https://fonts.googleapis.com/css2?family=Open+Sans:wght@700&family=Roboto+Condensed:wght@400;700&display=swap">
<style>
  :root{
    --page-bg:#ecebe8;
    --card-white:#ffffff;
    --card-silver:#e6e7e9;
    --panel-grey:#dcdddf;
    --panel-light:#eeeff0;
    --row-grey:#d8d9db;
    --brand-blue:#1b6fb5;
    --name-blue:#2e9be0;
    --edge-blue:#2a86c8;
    --text-dark:#2f3033;
    --text-mid:#55575b;
    --icon-bg:#c9cbce;
  }
  *{box-sizing:border-box;margin:0;padding:0}
  html,body{width:1200px;height:1023px;overflow:hidden;background:var(--page-bg)}
  .stage{position:relative;width:1200px;height:1023px}
  .card{
    position:absolute;left:150px;top:236px;width:900px;height:550px;
    background:linear-gradient(160deg,var(--card-white) 0%,var(--card-white) 45%,var(--card-silver) 100%);
    border-bottom:8px solid var(--edge-blue);
    box-shadow:0 14px 30px rgba(0,0,0,.18);
    overflow:hidden;
  }
  .panel-block{
    position:absolute;right:0;top:70px;width:260px;height:236px;
    background:linear-gradient(180deg,var(--panel-light),var(--panel-grey));
    border-bottom:6px solid var(--card-white);
  }
  .brand{
    position:absolute;left:60px;top:140px;display:flex;align-items:center;gap:18px;
  }
  .brand-dot{width:64px;height:64px;border-radius:50%;background:var(--brand-blue)}
  .brand-name{
    font-family:"Roboto Condensed",sans-serif;font-weight:700;font-size:46px;
    color:var(--brand-blue);text-transform:uppercase;letter-spacing:.5px;line-height:1;
  }
  .person{position:absolute;right:40px;top:56px;text-align:right}
  .person-name{
    font-family:"Open Sans",sans-serif;font-weight:700;font-size:34px;color:var(--name-blue);line-height:1.1;
  }
  .person-title{
    font-family:"Roboto Condensed",sans-serif;font-weight:400;font-size:24px;color:var(--text-dark);margin-top:4px;
  }
  .contacts{
    position:absolute;left:70px;right:0;top:330px;list-style:none;
    display:flex;flex-direction:column;gap:14px;
  }
  .contact-row{
    display:flex;align-items:center;gap:16px;height:50px;
    background:linear-gradient(90deg,rgba(216,217,219,.35),var(--row-grey));
    padding-left:10px;
  }
  .contact-icon{
    width:36px;height:36px;background:var(--icon-bg);display:flex;align-items:center;justify-content:center;flex:none;
  }
  .contact-text{
    font-family:"Roboto Condensed",sans-serif;font-size:22px;color:var(--text-mid);letter-spacing:.3px;
  }
</style>
</head>
<body>
<div class="stage">
  <section class="card" aria-label="Business card">
    <div class="panel-block"></div>

    <div class="brand">
      <span class="brand-dot"></span>
      <span class="brand-name">Skylark Learning Hub</span>
    </div>

    <div class="person">
      <p class="person-name">Lionel Tapping</p>
      <p class="person-title">Senior Education Consultant</p>
    </div>

    <ul class="contacts">
      <li class="contact-row">
        <span class="contact-icon">
          <svg width="22" height="22" viewBox="0 0 24 24" aria-hidden="true"><path fill="#1b6fb5" d="M6.6 10.8a15 15 0 0 0 6.6 6.6l2.2-2.2c.3-.3.7-.4 1-.2 1.1.4 2.3.6 3.6.6.6 0 1 .4 1 1V20c0 .6-.4 1-1 1A17 17 0 0 1 3 4c0-.6.4-1 1-1h3.5c.6 0 1 .4 1 1 0 1.3.2 2.5.6 3.6.1.3 0 .7-.2 1z"/></svg>
        </span>
        <span class="contact-text">0417 385 960</span>
      </li>
      <li class="contact-row">
        <span class="contact-icon">
          <svg width="22" height="22" viewBox="0 0 24 24" aria-hidden="true"><rect x="2" y="5" width="20" height="14" fill="#1b6fb5"/><path d="M2 5l10 8 10-8" fill="none" stroke="#fff" stroke-width="1.6"/></svg>
        </span>
        <span class="contact-text">Lionel.tapping@skylarklearninghub.com.au</span>
      </li>
      <li class="contact-row">
        <span class="contact-icon">
          <svg width="22" height="22" viewBox="0 0 24 24" aria-hidden="true"><circle cx="12" cy="12" r="10" fill="#1b6fb5"/><g fill="none" stroke="#fff" stroke-width="1.3"><ellipse cx="12" cy="12" rx="4.5" ry="10"/><path d="M2 12h20M4 7h16M4 17h16"/></g></svg>
        </span>
        <span class="contact-text">www.skylarklearninghub.com.au</span>
      </li>
    </ul>
  </section>
</div>
</body>
</html>
```